Letterhead designs for Property Management firm

Would like to see some different letterhead/envelope designs We are a residential property management company. We would like to see designs that utilize blue/grays/black

```html
<!DOCTYPE html>
<html lang="en">
<head>
<meta charset="utf-8">
<title>Harborview Property Management – Letterhead</title>
<link href="https://fonts.googleapis.com/css2?family=Arimo:wght@400;700&display=swap" rel="stylesheet">
<style>
  :root {
    --backdrop: #2a2c30;
    --paper: #f7f7f7;
    --ink: #6a6a6a;
    --ink-strong: #555555;
    --brand-blue: #1553a0;
    --accent-blue: #2b6f9f;
    --rule-blue: #5b95c6;
    --bar-gray: #8a8a8c;
  }
  * { box-sizing: border-box; margin: 0; padding: 0; }
  html, body { width: 1200px; height: 1200px; overflow: hidden; }
  body {
    background: var(--backdrop);
    font-family: "Arimo", Arial, sans-serif;
    color: var(--ink);
    position: relative;
  }
  .letterhead {
    position: absolute;
    left: 204px; top: 40px;
    width: 792px; height: 1120px;
    background: var(--paper);
    overflow: hidden;
  }
  .top-bar {
    position: absolute; left: 546px; top: 0; right: 0; height: 10px;
    background: var(--bar-gray);
  }
  .footer-band {
    position: absolute; left: 530px; right: 0; bottom: 0; height: 27px;
    background: var(--brand-blue);
  }
  .sidebar-rule {
    position: absolute; left: 552px; top: 50px; width: 1px; height: 993px;
    background: var(--rule-blue);
  }
  .letter {
    position: absolute; left: 58px; top: 112px; width: 454px;
    font-size: 12.8px; line-height: 18.6px;
  }
  .letter-date { margin-bottom: 36px; }
  .recipient { margin-bottom: 36px; }
  .recipient-name, .sign-title { font-weight: 700; color: var(--ink-strong); }
  .salutation { margin-bottom: 19px; }
  .letter-body p { text-align: justify; margin-bottom: 18.6px; }
  .closing { margin-top: 30px; }
  .signature {
    width: 172px; height: 24px; margin: -2px 0 -2px;
    background: linear-gradient(90deg, rgba(40,40,40,.08), rgba(40,40,40,.16), rgba(40,40,40,.06));
    border-radius: 12px;
  }
  .sidebar { position: absolute; left: 575px; width: 200px; font-size: 12.8px; line-height: 16px; }
  .brand {
    top: 36px; left: 585px; width: 180px;
    display: flex; align-items: center; gap: 10px;
    color: var(--brand-blue); font-weight: 700; font-size: 17px; line-height: 20px;
  }
  .brand-square { width: 26px; height: 26px; background: var(--brand-blue); flex: none; }
  .dash { width: 12px; height: 2px; background: var(--accent-blue); margin-bottom: 10px; }
  .sender { top: 243px; }
  .sender-name { color: var(--accent-blue); font-weight: 700; font-size: 16px; line-height: 18px; }
  .contact { top: 328px; }
  .sidebar-heading { color: var(--accent-blue); font-weight: 700; }
  .contact-line { display: flex; align-items: center; gap: 6px; }
  .contact-line svg { width: 10px; height: 10px; flex: none; }
  .address { top: 954px; }
  .address-company { color: var(--brand-blue); }
</style>
</head>
<body>
  <main class="letterhead">
    <div class="top-bar"></div>
    <div class="sidebar-rule"></div>

    <section class="letter">
      <p class="letter-date">January 1, 2050</p>
      <div class="recipient">
        <p class="recipient-name">Laura Bennett</p>
        <p>Managing Director</p>
        <p>Co.Street, Building/Suite</p>
        <p>City/State, Zip Code</p>
      </div>
      <p class="salutation">Dear Laura Bennett,</p>
      <div class="letter-body">
        <p>Lorem ipsum dolor sit amet, consectetuer adipiscing elit, sed diam nonummy nibh euismod tincidunt ut laoreet dolore magna aliquam erat volutpat. Ut wisi enim ad minim veniam, quis nostrud exerci tation ullamcorper suscipit lobortis nisl ut aliquip ex ea commodo consequat. Duis dolore te feugait nulla facilisi. Nam liber tempor cum soluta nobis eleifend option congue nihil imperdiet doming id quod mazim placerat facer possim assum.</p>
        <p>Consectetuer adipiscing elit, sed diam nonummy nibh euismod tincidunt ut laoreet dolore magna aliquam erat volutpat. Ut wisi enim ad minim veniam, quis nostrud exerci tation ullamcorper suscipit lobortis nisl ut aliquip ex ea commodo consequat. Consectetuer adipiscing elit, sed diam nonummy nibh euismod tincidunt ut laoreet dolore magna aliquam erat volutpat. Ut wisi enim ad minim veniam, quis nostrud exerci tation ullamcorper suscipit lobortis nisl ut aliquip ex ea commodo consequat.</p>
        <p>Duis dolore te feugait nulla facilisi. Nam liber tempor cum soluta nobis eleifend option congue nihil imperdiet doming id quod mazim placerat facer possim assum.Duis dolore te feugait nulla facilisi. Nam liber tempor cum soluta nobis eleifend option congue nihil imperdiet doming id quod mazim placerat facer possim assum.</p>
      </div>
      <div class="closing">
        <p>Sincerely Yours,</p>
        <div class="signature" role="img" aria-label="Handwritten signature of the managing director"></div>
        <p class="sign-title">Authorized Managing Director</p>
        <p>Your Company Name</p>
      </div>
    </section>

    <div class="sidebar brand">
      <span class="brand-square"></span>
      <span>Harborview Property Management</span>
    </div>

    <div class="sidebar sender">
      <div class="dash"></div>
      <p class="sender-name">Daniel Whitford</p>
      <p>Managing Director</p>
    </div>

    <div class="sidebar contact">
      <div class="dash"></div>
      <p class="sidebar-heading">Contact:</p>
      <p class="contact-line">
        <svg viewBox="0 0 10 10"><path d="M2 1 L4 1 L4.6 3.2 L3.4 4 Q4.3 5.9 6 6.6 L6.8 5.4 L9 6 L9 8 Q5 9.5 1.5 5 Q0.8 3 2 1Z" fill="#2b6f9f"/></svg>
        555.010.2040
      </p>
      <p class="contact-line">
        <svg viewBox="0 0 10 10"><rect x="0.8" y="2" width="8.4" height="6" fill="none" stroke="#2b6f9f" stroke-width="1"/><path d="M0.8 2 L5 5.4 L9.2 2" fill="none" stroke="#2b6f9f" stroke-width="1"/></svg>
        hello@harborviewpm.com
      </p>
      <p class="contact-line">
        <svg viewBox="0 0 10 10"><circle cx="5" cy="5" r="4.2" fill="none" stroke="#2b6f9f" stroke-width="1"/><ellipse cx="5" cy="5" rx="1.8" ry="4.2" fill="none" stroke="#2b6f9f" stroke-width=".8"/><path d="M0.8 5 H9.2" stroke="#2b6f9f" stroke-width=".8"/></svg>
        www.harborviewpm.com
      </p>
    </div>

    <div class="sidebar address">
      <div class="dash"></div>
      <p class="sidebar-heading">Address:</p>
      <p class="address-company">Harborview Property Management</p>
      <p>Co.Street, Building/Suite 12345</p>
      <p>City/State, Zip Code</p>
    </div>

    <div class="footer-band"></div>
  </main>
</body>
</html>
```